Dietetic office: Bright Plate

I want to give my business card a modern and warm look (which attracts the eye and has a reassuring side), which links dietetics to a moment of well-being. The front and back sides must be used (not just to put the logo on the front side)

The map should be eye-catching and easy to read. I don't necessarily want to have a plain background, which I find visually weighs down the maps.
I really like the square format of a business card with rounded edges which is different from what we are used to finding (and why not take this square diagonally?), however I am not closed to another format as long as I like the style.

Who am I? Mireille, 32 years old, Dietician and passionate about food since always. I am specialized in slimming and an expert in micro nutrition, which means that I take into account not only the nutritional balance while maintaining pleasure (if foods are present in the business card, I do not want some cliché things where there would just be fruits and vegetables, but really something more global), but also the psycho-emotional dimension that I will treat with food supplements based on plants, fruits or vegetables.

-----------------------------------------------------------------------------------

 Mention to appear on the card IN FRENCH (please be careful in case of translation that the use of words is correct):

Mireille DORAN
Dietician Nutritionist
Expert in Slimming and Micro-Nutrition

Slogan: I help you lose weight sustainably with pleasure and by reconciling your events

Catchphrases: Want to lose weight? Do you like going out? Do you have a lot of events? And is pleasure on your plate important to you?

Make an appointment on Rendiplan or on 06 41 58 30 92
mireille.brightplate@exemplo-mail.fr
Address: Health Center, Rue des Glycines, 13127 Vitrolles
www.brightplate-exemple.fr
Friendwall + Picturo Logo

- The company logo has been uploaded for your viewing. Other file formats can be made available if required.
- I would like a place for a photo of me to be possible.

Good morning,
I want to have a business card that is both lively and warm. Which will easily catch the eye while being easy to read and make people understand that I am in the field of well-being.
I like the square side in business cards (and why not use them diagonally?), or a more classic but original one.
Both the front and back sides must be used (I don't want to have the logo on just one side)
I don't want to have a plain background, but rather something more muted (I really like the suggestion from "Reed Cloud Graphic Designer" for this)
the use of logo for telephone, mail, address, rendiplan, friendwall, pictu etc is possible in order to facilitate reading

Please follow the various elements of the brief regarding the text and use the French text as it is.

I like business cards preferably square (with the possibility of using them diagonally).
The map should be eye-catching and easy to read.
It must bring pep while having softness which brings back to the well-being side
The card must be used on the front and back for the different elements (I do not want to have only the logo on the front side)
The text must correspond to the brief (be careful with the translation which can sometimes be bad)
I don't want to have a plain blue or orange background. I really like the idea of the background from "Reed Cloud Graphic Designer"

You can if you wish use symbols for contacts, telephone, rendiplan, address, fw, pictu....

Target Market(s)

mainly women between 25 and 65 years old + men around 40 years old

Contact Information for Business Card

Font styles to use
Sans Serif
Script

Colors
0054AA
0677BA
7BADD7
CADEEF
E8F1F8
0094D4
00A9DD
6FCCEA
C7EBF8
E9F6FB
00AB8E
00BBA5
67D7C9
C6EFE9
E9F9F6
FFC000
F8CF3A
FAE287
FDF2CF
FEFAEE
F0912C
F2A743
F7CA91
FBE8D2
FDF5EE

Requirements
Must have
• some pep! while being refined
Nice to have
• I really like the square format of a business card with rounded edges which is different from what we are used to finding, however I am not closed to another format as long as I like the style.
Should not have
• if foods are represented, only show fruits and vegetables (too cliché)

```html
<!DOCTYPE html>
<html lang="fr">
<head>
<meta charset="utf-8">
<title>Bright Plate – Carte de visite</title>
<link rel="stylesheet" href="https://fonts.googleapis.com/css2?family=Arimo:ital,wght@0,400;0,700;1,400&display=swap">
<style>
  :root {
    --page-bg: #e8e8e8;
    --card-bg: #ffffff;
    --brand-blue: #0a79d3;
    --accent-orange: #f7931e;
    --accent-cyan: #1cc7da;
    --ink: #222222;
    --white: #ffffff;
  }
  * { margin: 0; padding: 0; box-sizing: border-box; }
  html, body {
    width: 764px; height: 1200px; overflow: hidden;
    background: var(--page-bg);
    font-family: "Arimo", Arial, sans-serif;
  }
  .canvas { position: relative; width: 764px; height: 1200px; }
  .card {
    position: absolute; left: 157px; width: 463px; height: 463px;
    background: var(--card-bg); border-radius: 20px; overflow: hidden;
  }
  .card--front { top: 88px; }
  .card--back { top: 631px; }
  .card__shapes { position: absolute; inset: 0; width: 463px; height: 463px; }
  .brand-name {
    position: absolute; color: var(--brand-blue);
    font-size: 30px; font-weight: 400; letter-spacing: 0.5px; white-space: nowrap;
  }
  .card--front .brand-name { left: 30px; top: 66px; }
  .card--back .brand-name { right: 22px; top: 70px; }
  .social-links {
    position: absolute; right: 24px; top: 22px;
    display: flex; gap: 8px; font-size: 11px; color: var(--brand-blue);
  }
  .person-name {
    position: absolute; left: 28px; top: 138px;
    font-size: 25px; font-weight: 700; color: var(--brand-blue);
  }
  .person-title {
    position: absolute; left: 28px; top: 171px;
    font-size: 15px; color: var(--accent-orange);
  }
  .person-speciality {
    position: absolute; left: 28px; top: 197px;
    font-size: 13.5px; color: var(--ink);
  }
  .contact-list { position: absolute; left: 28px; top: 230px; list-style: none; }
  .contact-item {
    display: flex; align-items: flex-start; gap: 12px;
    font-size: 15px; line-height: 21px; color: var(--ink);
  }
  .contact-item + .contact-item { margin-top: 1px; }
  .contact-item--address { margin-top: 12px !important; }
  .contact-icon { width: 16px; height: 16px; flex: none; margin-top: 3px; fill: var(--accent-cyan); }
  .slogan {
    position: absolute; left: 0; right: 0; top: 400px;
    text-align: center; font-style: italic; font-size: 16.5px; line-height: 23px;
    color: var(--white);
  }
  .questions {
    position: absolute; left: 22px; top: 110px;
    font-style: italic; font-size: 20px; line-height: 27.6px; color: var(--white);
  }
  .appointment {
    position: absolute; left: 24px; top: 393px;
    font-size: 13.5px; font-weight: 700; line-height: 19px; color: var(--accent-orange);
  }
</style>
</head>
<body>
<main class="canvas">

  <section class="card card--front" aria-label="Recto de la carte">
    <svg class="card__shapes" viewBox="0 0 463 463" aria-hidden="true">
      <path d="M0,376 C170,392 380,350 463,172 L463,463 L0,463 Z" fill="var(--brand-blue)"/>
      <path d="M0,368 C175,382 385,338 463,168" fill="none" stroke="var(--accent-cyan)" stroke-width="4"/>
      <path d="M150,382 C280,372 420,320 463,185" fill="none" stroke="var(--accent-orange)" stroke-width="4"/>
    </svg>

    <div class="social-links"><span>Picturo</span><span>Friendwall</span></div>
    <div class="brand-name">Bright Plate</div>

    <h1 class="person-name">Mireille DORAN</h1>
    <p class="person-title">Diététiste Nutritionniste</p>
    <p class="person-speciality">Expert en Minceur et Micro-Nutrition</p>

    <ul class="contact-list">
      <li class="contact-item">
        <svg class="contact-icon" viewBox="0 0 16 16"><path d="M1 3h14v10H1z"/><path d="M1.5 3.5l6.5 5.5 6.5-5.5" fill="none" stroke="#fff" stroke-width="1.2"/></svg>
        <span>mireille.brightplate@exemplo-mail.fr</span>
      </li>
      <li class="contact-item">
        <svg class="contact-icon" viewBox="0 0 16 16"><circle cx="8" cy="8" r="7.5"/><path d="M1 8h14M8 1c-3 3-3 11 0 14M8 1c3 3 3 11 0 14" fill="none" stroke="#fff" stroke-width="1"/></svg>
        <span>www.brightplate-exemple.fr</span>
      </li>
      <li class="contact-item contact-item--address">
        <svg class="contact-icon" viewBox="0 0 16 22" style="height:21px"><path d="M8 0a7.5 7.5 0 0 0-7.5 7.5C0.5 13 8 22 8 22s7.5-9 7.5-14.5A7.5 7.5 0 0 0 8 0z"/><circle cx="8" cy="7.5" r="3" fill="#fff"/></svg>
        <span>Espace Santé Horizon<br>Rue des Glycines<br>13990 Valmorel</span>
      </li>
    </ul>

    <p class="slogan">Je vous aide à perdre du poids durablement avec<br>plaisir et en réconciliant vos événements</p>
  </section>

  <section class="card card--back" aria-label="Verso de la carte">
    <svg class="card__shapes" viewBox="0 0 463 463" aria-hidden="true">
      <path d="M96,0 C300,150 390,300 350,390 C330,430 290,450 240,463" fill="none" stroke="var(--accent-orange)" stroke-width="11"/>
      <path d="M82,0 C285,150 372,300 336,388 C318,428 280,448 230,463" fill="none" stroke="var(--accent-cyan)" stroke-width="6"/>
      <path d="M0,0 L78,0 C280,150 366,300 330,388 C314,426 278,446 228,463 L0,463 Z" fill="var(--brand-blue)"/>
      <rect x="0" y="386" width="330" height="52" fill="var(--card-bg)"/>
    </svg>

    <div class="brand-name">Bright Plate</div>

    <p class="questions">Je veux<br>perdre poids?<br>Est-ce que tu<br>aimes aller dehors?<br>Avez-vous beaucoup<br>de événements?<br>Et le plaisir sur<br>votre assiette est<br>importante pour vous?</p>

    <p class="appointment">Prenez rendez-vous sur Rendiplan<br>ou au 06 41 58 30 92</p>
  </section>

</main>
</body>
</html>
```